Cover for Every door Opens Where Every Door Opens

Book Cover Request
Format: Print and electronic (Quillmart)
Book Title: Every Door Opens Where Every Door Opens: Practical Roadmap for Courage and Progress
Author: R.K. Vantreel
Description: This self-help book, written by me, a self-proclaimed nobody, is filled with actionable insights and proven strategies that can help anyone. It combines humor with a serious undertone to deliver practical advice without the typical "self-helpy" vibe.
Catchphrase for the Cover: "Go from Oh Shit to Crushing It!" (or something similar)
Style: I want the cover to reflect my personality—funny, yet serious when needed. I'm open to suggestions and would love to see a design that captures the essence of the book without being too typical of the self-help genre.
Additional Information: I've attached a rough draft of the Quillmart description for more context.
Thank you for your help!
Target Market(s)
Anyone. but id say over 25
Requirements
Nice to have
- Honestly im really at a loss. Im hoping the description will help guide you. I gues i would like it to satand out of course. Be diffrent....but i know how crazy that sounds because everyone wants that. Just give me soem ideas!

```html
<!DOCTYPE html>
<html lang="en">
<head>
<meta charset="utf-8">
<title>Every Door Opens Where Every Door Opens — R.K. Vantreel</title>
<link rel="stylesheet" href="https://fonts.googleapis.com/css2?family=Amatic+SC:wght@700&family=Roboto:wght@400;700&display=swap">
<style>
  :root {
    --sky-top: #1f8ccc;
    --sky-mid: #1680c2;
    --sky-deep: #0e72b2;
    --ink-white: #ffffff;
    --ink-blue: #1b78b4;
    --brush-white: #fbfdff;
  }
  * { margin: 0; padding: 0; box-sizing: border-box; }
  html, body {
    width: 750px;
    height: 1200px;
    overflow: hidden;
    background: var(--sky-mid);
  }
  .cover {
    position: relative;
    width: 750px;
    height: 1200px;
    overflow: hidden;
  }
  .cover-scene {
    position: absolute;
    inset: 0;
    background:
      radial-gradient(ellipse 200px 560px at 610px 700px, rgba(130,195,238,0.32), transparent 70%),
      linear-gradient(180deg, var(--sky-top) 0%, var(--sky-mid) 50%, var(--sky-deep) 100%);
  }
  .title {
    position: absolute;
    left: 30px;
    top: 62px;
    width: 460px;
    font-family: "Amatic SC", "Arial Narrow", cursive;
    font-weight: 700;
    color: var(--ink-white);
    font-size: 112px;
    line-height: 116px;
    letter-spacing: 2px;
    text-transform: uppercase;
    text-align: center;
  }
  .title span { display: block; white-space: nowrap; }
  .subtitle-brush {
    position: absolute;
    left: 24px;
    top: 728px;
    width: 466px;
    height: 270px;
  }
  .subtitle {
    position: absolute;
    left: 148px;
    top: 790px;
    width: 300px;
    font-family: "Roboto", Arial, sans-serif;
    font-weight: 400;
    font-size: 31px;
    line-height: 36px;
    color: var(--ink-blue);
    text-transform: uppercase;
    letter-spacing: 0.5px;
    transform: rotate(-11deg);
    transform-origin: left top;
  }
  .subtitle span { display: block; white-space: nowrap; }
  .subtitle strong { font-weight: 700; }
  .author {
    position: absolute;
    left: 40px;
    top: 1034px;
    width: 440px;
    text-align: center;
    white-space: nowrap;
    font-family: "Amatic SC", "Arial Narrow", cursive;
    font-weight: 700;
    font-size: 84px;
    line-height: 100px;
    letter-spacing: 2px;
    color: var(--ink-white);
    text-transform: uppercase;
  }
</style>
</head>
<body>
  <main class="cover">
    <div class="cover-scene" role="img" aria-label="Photograph of a bright blue wall; on the right a man in white clothes stands on a wooden ladder, using a paint roller to paint a white ladder continuing up the wall"></div>

    <h1 class="title">
      <span>Every Door</span>
      <span>Opens</span>
      <span>Where</span>
      <span>Every Door</span>
      <span>Opens</span>
    </h1>

    <svg class="subtitle-brush" viewBox="0 0 466 270" aria-hidden="true">
      <path fill="var(--brush-white)" d="M60 60 C120 30 200 24 270 14 C330 6 380 4 440 10 C452 14 450 24 436 30 C466 40 462 62 444 74 C460 96 452 120 436 134 C456 150 446 170 420 180 C396 200 340 212 280 222 C230 232 190 242 150 254 C120 264 100 266 110 252 C80 254 52 248 44 236 C60 228 72 222 62 214 C30 212 14 200 30 190 C8 184 2 172 20 164 C40 156 30 148 24 140 C14 128 26 116 44 110 C22 100 28 86 46 80 C34 74 42 64 60 60 Z"/>
    </svg>

    <p class="subtitle">
      <span>Practical</span>
      <span>Roadmap</span>
      <span>For <strong>Courage</strong></span>
      <span>And <strong>Progress</strong></span>
    </p>

    <p class="author">R.K. Vantreel</p>
  </main>
</body>
</html>
```